Photobook template design

Just one book of 4/5 pages needed to find a handful of designers to help with this project that will be ongoing for several months, we will agree design price per book.

Hi there, we need lots of fabulous photobook templates designed:
there will be 20 books to start with, canvas layouts, calendar layouts etc.

The MAIN idea of the template is to facilitate the easiest creation / ordering of photobooks etc. possible for the client, so all they have to do is upload their pics and drop them into the templates you're going to design...

Each photobook needs to have min 20 pages, there can be a common theme throughout, but they must be different enough so that they do not all blend into one.
Choose to create a design from the following categories:
family
kids
travel
romance / love
seasonal holiday
year in review
everyday / general
recipes
pets / animals
collage
scrapbook

the quality and look and feel must be equal to www.pagelark.com / www.snapvellum.com / www.printorra.co.uk

In order to keep the designs as fresh as possible - we will work with several designers, so for this first project we will choose 1 designer, but then we'll create other design projects for which you will be specifically invited to design for - it's the only way the do multiple designs/projects.

please see 2 pics attached of other templates already designed - we're very happy with these...

Target Market(s)

These photobooks / calendars / canvas prints are for the average family - not too serious, must be fun / tongue in cheek etc.
They're for people who want to do photobooks but have no clue or do not have the time - so they must LOVE the design, and then want to just add their photos...

Industry/Entity Type

Travel

Requirements
Must have
• Must be designed in Layoutra or Vectorix.
Metric sizes please - Either A3 landscape or portrait with 3 mm bleed, or 300 x 300mm square - 3mm bleed
If you place photos for proofing, please use imagewell images - we have a imagewell account

```html
<!DOCTYPE html>
<html lang="en">
<head>
<meta charset="utf-8">
<title>My Recipe Book – Photobook Template</title>
<link rel="stylesheet" href="https://fonts.googleapis.com/css2?family=Cabin:wght@400;500;600&family=Lora:wght@400&family=Open+Sans:ital,wght@0,400;0,700;1,400&display=swap">
<style>
:root{
  --table:#b5835a;
  --table-dark:#8f6440;
  --page:#ffffff;
  --ink:#2b2b2b;
  --title-maroon:#9c2a35;
  --brown:#8a5a3c;
  --red:#e0262a;
  --coral:#e8452c;
  --green:#7dbb2f;
  --orange:#f4a11e;
  --leaf:#2fae4a;
  --sky:#2aa6de;
  --slate:#4a6c96;
  --purple:#8e2a8f;
  --pink:#d8246e;
}
*{box-sizing:border-box;margin:0;padding:0}
html,body{width:1200px;height:1144px;overflow:hidden}
body{
  position:relative;
  background:linear-gradient(90deg,var(--table) 0%,#c08f63 40%,var(--table-dark) 100%);
  font-family:"Open Sans",Arial,sans-serif;color:var(--ink);
}
.sheet{position:absolute;background:var(--page);overflow:hidden}
.photo{position:absolute}
.heading{
  position:absolute;left:0;right:0;height:22px;padding:2px 6px;
  font-family:"Cabin",Arial,sans-serif;font-weight:500;font-size:14px;color:#fff;line-height:18px;
  white-space:nowrap;overflow:hidden;
}
.heading.compact{font-size:13px}
.label{font-family:"Cabin",Arial,sans-serif;font-weight:600;font-size:8px;line-height:10px;display:block;margin-bottom:1px;font-style:normal}
.ingredients{position:absolute;font-size:6.3px;line-height:7.4px;font-style:italic}
.cols{display:flex;gap:10px}
.cols div{flex:1}
.method{position:absolute;font-size:6.2px;line-height:7.6px}
.frame{border:3px solid}

/* cover */
.cover{left:40px;top:101px;width:558px;height:398px;background:linear-gradient(90deg,#b07a4d,#c89a6c 50%,#a87248);}
.cover-photo{left:279px;top:0;width:279px;height:398px;background:radial-gradient(ellipse at 45% 55%,#c9a06c 0%,#a97a4d 45%,#6c7a35 80%,#8e3a25 100%)}
.cover-title{
  position:absolute;left:362px;top:112px;width:120px;text-align:center;
  font-family:"Lora",Georgia,serif;font-weight:400;font-size:40px;line-height:44px;color:var(--title-maroon);
}
</style>
</head>
<body>

<!-- Cover -->
<section class="sheet cover">
  <div class="photo cover-photo" role="img" aria-label="Cutting board on wood surrounded by spices, herbs, wooden spoons and vegetables"></div>
  <h1 class="cover-title">My recipe book</h1>
</section>

<!-- Blueberry / beef page -->
<section class="sheet" style="left:40px;top:553px;width:558px;height:394px;border:3px solid var(--purple)">
  <div class="photo" style="left:0;top:0;width:300px;height:388px;background:linear-gradient(160deg,#d8dde3,#8aa3b8 45%,#b98c5a 75%,#4e5f78)" role="img" aria-label="Blueberry muffins in paper cases on a blue cloth"></div>
  <div class="heading" style="left:303px;top:0;background:var(--purple)">Blueberry Muffin</div>
  <div class="ingredients" style="left:309px;top:28px;width:235px">
    <span class="label" style="color:var(--purple)">Ingredients:</span>
    <div class="cols"><div>2 c. fresh blueberries<br>2 eggs<br>2 c. flour<br>1 c. sugar<br>1/2 c. milk</div><div>1/4 c. butter<br>2 tsp baking powder<br>1 tsp vanilla<br>1/2 tsp salt</div></div>
  </div>
  <div class="method" style="left:309px;top:82px;width:235px"><span class="label" style="color:var(--purple)">Preparation:</span>Preheat oven to 350F. Grease a muffin pan. Combine flour, sugar and baking powder, then stir in butter, eggs and milk. Fold in the blueberries. Fill cups two thirds full and bake 20 to 25 minutes until golden.</div>
  <div class="heading compact" style="left:303px;top:138px;background:var(--pink)">Beef Tenderloin With Roasted Shallots</div>
  <div class="ingredients" style="left:309px;top:166px;width:235px">
    <span class="label" style="color:var(--pink)">Ingredients:</span>
    <div class="cols"><div>3/4 pound shallots, halved lengthwise and peeled<br>1 1/2 tablespoons olive oil<br>salt and pepper to taste<br>3 cups beef broth<br>3/4 cup port wine<br>3 slices bacon, diced<br>1 teaspoon dried thyme</div><div>1 1/2 teaspoons tomato paste<br>2 pounds beef tenderloin roast, trimmed<br>3 tablespoons butter<br>1 tablespoon all-purpose flour<br>4 sprigs watercress, for garnish</div></div>
  </div>
  <div class="photo frame" style="left:305px;top:258px;width:244px;height:78px;border-color:var(--pink);background:linear-gradient(90deg,#3a2418,#7a4a2c 50%,#4b3020)" role="img" aria-label="Sliced beef tenderloin with roasted shallots"></div>
  <div class="method" style="left:309px;top:342px;width:235px"><span class="label" style="color:var(--pink)">Preparation:</span>Preheat oven to 375 degrees. Toss shallots with oil, season and roast until tender. Sear the beef in a hot pan, then roast until done to your liking.</div>
</section>

<!-- Chicken -->
<section class="sheet" style="left:641px;top:0;width:257px;height:380px">
  <div class="heading" style="top:4px;background:var(--brown)">Hot Beer Butt Chicken</div>
  <div class="ingredients" style="left:8px;top:34px;width:240px">
    <span class="label" style="color:#d36b1f">Ingredients:</span>1 cup butter<br>2 tablespoons garlic salt<br>2 tablespoons paprika<br>salt and pepper to taste<br>1 (12 fluid ounce) can beer<br>1 (4 pound) whole chicken
  </div>
  <div class="photo" style="left:8px;top:146px;width:241px;height:156px;background:radial-gradient(ellipse at 50% 60%,#8a3a14,#4a1a08 55%,#1a0c05)" role="img" aria-label="Roast chicken on a grill with flames and herbs"></div>
  <div class="method" style="left:8px;top:308px;width:241px"><span class="label" style="color:#d36b1f">Preparation:</span>Preheat an outdoor grill for low heat. In a small skillet, melt the butter and stir in garlic salt and paprika. Set the can of beer inside the chicken and brush with the butter mix. Stand the bird on the grill, cover and cook about 3 hours, until the juices run clear.</div>
</section>

<!-- Lasagna -->
<section class="sheet" style="left:903px;top:0;width:264px;height:380px">
  <div class="heading" style="top:4px;background:var(--red)">The Best Lasagna Ever</div>
  <div class="ingredients" style="left:6px;top:32px;width:252px;font-style:normal">
    <span class="label" style="color:var(--red)">Ingredients:</span>
    <div class="cols"><div>1-1/2 pound Ground Beef<br>1 pound Hot Breakfast Sausage<br>2 cloves Garlic, Minced<br>2 cans (14.5 Ounce) Whole Tomatoes<br>2 cans (6 Ounce) Tomato Paste<br>2 Tablespoons Dried Parsley<br>2 Tablespoons Dried Basil<br>1 teaspoon Salt<br>3 cups Lowfat Cottage Cheese</div><div>2 whole Beaten Eggs<br>1/2 cup Grated Parmesan Cheese<br>2 Tablespoons Dried Parsley<br>1 teaspoon Salt<br>1 pound Sliced Mozzarella Cheese<br>1 package Lasagna Noodles<br>Olive Oil To Pasta Water</div></div>
  </div>
  <div class="photo frame" style="left:4px;top:114px;width:256px;height:146px;border-color:var(--red);background:radial-gradient(ellipse at 50% 55%,#e08a3a,#b8401a 55%,#6a1a0a)" role="img" aria-label="Slice of layered lasagna with melted cheese"></div>
  <div class="method" style="left:6px;top:266px;width:252px"><span class="label" style="color:var(--red)">Preparation:</span>Bring a large pot of water to a boil. Brown the beef and sausage with garlic, then add tomatoes, paste, parsley and basil and simmer 45 minutes. Mix cottage cheese, eggs and Parmesan. Layer noodles, cheese mix, mozzarella and sauce in a baking pan. Bake at 350 degrees for 20 to 30 minutes until hot and bubbly.</div>
</section>

<!-- Strawberry -->
<section class="sheet" style="left:641px;top:386px;width:257px;height:372px">
  <div class="heading" style="top:2px;background:var(--coral)">Strawberry and Cream Sponge Cake</div>
  <div class="ingredients" style="left:8px;top:29px;width:240px">
    <span class="label" style="color:var(--coral)">Ingredients:</span>3 large free-range eggs at room temperature<br>225g/8oz caster sugar<br>225g/8oz self-raising flour + 2 tsp baking powder<br>125g/4oz softened butter<br>100g/3 oz margarine<br>225g/8oz fresh strawberries, washed and sliced<br>200ml/7 fl oz whipping cream, whipped to firm peaks
  </div>
  <div class="photo frame" style="left:6px;top:98px;width:244px;height:152px;border-color:var(--coral);background:radial-gradient(ellipse at 45% 55%,#f4e6d4,#e07a6a 50%,#c9d2da)" role="img" aria-label="Slice of sponge cake filled with cream and strawberries"></div>
  <div class="method" style="left:8px;top:256px;width:241px"><span class="label" style="color:var(--coral)">Preparation:</span>Preheat the oven to 180C. Grease and line two 20cm sandwich tins. Beat the eggs, sugar, flour, baking powder and butter until smooth. Divide between the tins and bake for 20 minutes until golden. Cool on a rack. Spread one cake with cream and sliced strawberries, then top with the second cake.</div>
</section>

<!-- Paella -->
<section class="sheet" style="left:903px;top:386px;width:264px;height:372px">
  <div class="heading" style="top:2px;background:var(--green)">Perfect paella</div>
  <div class="ingredients" style="left:6px;top:29px;width:252px">
    <span class="label" style="color:var(--green)">Ingredients:</span>
    <div class="cols"><div>8 raw, unshelled tiger prawns<br>90ml olive oil<br>3 cloves garlic, finely chopped<br>500ml good-quality fish stock<br>150g monkfish, cut into chunks<br>1 onion, finely diced<br>1 tsp smoked paprika<br>200g chopped tomatoes</div><div>50ml dry white wine<br>Pinch of saffron<br>200g short-grain rice<br>150g baby squid<br>150g broad beans<br>150g mussels, scrubbed<br>Handful of flat-leaf parsley<br>½ lemon, cut into wedges</div></div>
  </div>
  <div class="photo frame" style="left:4px;top:98px;width:256px;height:152px;border-color:var(--green);background:radial-gradient(ellipse at 50% 55%,#f0b43a,#c06a1a 55%,#3a2a1a)" role="img" aria-label="Pan of seafood paella with prawns and mussels"></div>
  <div class="method" style="left:6px;top:256px;width:252px"><span class="label" style="color:var(--green)">Preparation:</span>Shell the prawns and set aside. Heat oil in a large pan and gently fry the onion and garlic until soft. Add the rice, paprika and saffron, then pour in the stock and wine. Simmer without stirring, add the seafood and cook until the rice is tender. Finish with parsley and lemon wedges.</div>
</section>

<!-- Waffles & omelet column -->
<section class="sheet" style="left:641px;top:764px;width:174px;height:380px">
  <div class="heading" style="top:4px;background:var(--orange)">Waffles</div>
  <div class="ingredients" style="left:6px;top:30px;width:164px">
    <span class="label" style="color:var(--orange)">Ingredients:</span>
    <div class="cols" style="gap:4px"><div>eggs<br>2 cups all-purpose flour<br>1 3/4 cups milk<br>1/2 cup vegetable oil<br>1 tablespoon white sugar</div><div>4 teaspoons baking powder<br>1/4 teaspoon salt<br>1/2 teaspoon vanilla extract</div></div>
  </div>
  <div class="photo frame" style="left:4px;top:110px;width:166px;height:84px;border-color:var(--orange);background:radial-gradient(ellipse at 50% 55%,#e8b45a,#d8454a 50%,#f4efe8)" role="img" aria-label="Waffles topped with berries on a plate"></div>
  <div class="method" style="left:6px;top:198px;width:164px"><span class="label" style="color:var(--orange)">Preparation:</span>Preheat waffle iron. Beat eggs, then add flour, milk, oil, sugar, baking powder, salt and vanilla. Pour onto hot iron and cook until golden brown.</div>
  <div class="heading" style="top:254px;background:var(--leaf)">Baked Brunch Omelet</div>
  <div class="ingredients" style="left:6px;top:282px;width:164px">
    <span class="label" style="color:var(--leaf)">Ingredients:</span>1/2 (1 pound) loaf white bread, cut into cubes<br>1 1/2 pounds Cheddar cheese, shredded<br>1 cup cubed cooked ham<br>8 eggs<br>2 cups milk<br>1 pinch salt<br>1 dash hot pepper sauce, or to taste<br>3/4 cup chopped green onion
  </div>
</section>

<!-- Omelet photo & tacos column -->
<section class="sheet" style="left:818px;top:764px;width:164px;height:380px">
  <div class="photo" style="left:0;top:0;width:164px;height:106px;background:radial-gradient(ellipse at 50% 60%,#f4d27a,#e8b04a 45%,#5a8a3a 80%,#f2f2f2)" role="img" aria-label="Baked omelet with tomatoes and herbs on a white plate"></div>
  <div class="method" style="left:6px;top:110px;width:154px"><span class="label" style="color:var(--leaf)">Preparation:</span>Preheat oven to 350 F. Place bread cubes in a baking dish and top with cheese. Beat eggs and milk and pour over. Bake 40 minutes.</div>
  <div class="heading compact" style="top:178px;background:var(--sky)">Mexican Breakfast Tacos</div>
  <div class="ingredients" style="left:6px;top:204px;width:154px">
    <span class="label" style="color:var(--sky)">Ingredients:</span>
    <div class="cols" style="gap:4px"><div>6 ounces chorizo sausage<br>8 (6 inch) corn tortillas<br>6 eggs<br>1/4 cup milk<br>1/2 teaspoon pepper<br>1/2 teaspoon salt<br>1/2 cup shredded Monterey Jack cheese</div><div>1 dash hot pepper sauce (e.g. Redfire)<br>1/2 cup salsa<br>2 cups milk<br>1 pinch salt<br>1 dash hot pepper sauce<br>1/4 cup chopped green onion</div></div>
  </div>
  <div class="photo frame" style="left:2px;top:290px;width:160px;height:86px;border-color:var(--sky);background:radial-gradient(ellipse at 50% 55%,#e8c890,#a6763a 50%,#3a4a3a)" role="img" aria-label="Breakfast tacos with egg and chorizo"></div>
</section>

<!-- Tacos method & pancake column -->
<section class="sheet" style="left:985px;top:764px;width:182px;height:380px">
  <div class="method" style="left:6px;top:6px;width:170px"><span class="label" style="color:var(--sky)">Preparation:</span>Crumble the sausage into a skillet and cook until browned. Warm the tortillas. Whisk the eggs with milk, salt and pepper, then scramble until set. Fill each tortilla with egg, sausage, cheese and onion, and add hot sauce to taste.</div>
  <div class="heading" style="top:106px;background:var(--slate)">Pancake</div>
  <div class="ingredients" style="left:6px;top:132px;width:170px">
    <span class="label" style="color:var(--sky)">Ingredients:</span>
    <div class="cols" style="gap:4px"><div>250 g Plain Flour<br>2 Eggs<br>400 ml Fresh Milk</div><div>Pinch of Salt<br>Sunflower Oil for frying</div></div>
  </div>
  <div class="photo frame" style="left:4px;top:174px;width:174px;height:100px;border-color:var(--sky);background:radial-gradient(ellipse at 50% 55%,#e8b06a,#c0283a 45%,#3a3a6a 75%,#eef2f6)" role="img" aria-label="Stack of pancakes with mixed berries"></div>
  <div class="method" style="left:6px;top:280px;width:170px"><span class="label" style="color:var(--sky)">Preparation:</span>Sift the flour into a bowl with the salt. Break in the eggs and whisk in the milk to a smooth batter. Heat a little oil in a pan, pour in a thin layer and cook until golden on both sides.</div>
</section>

</body>
</html>
```